Business Card and Letterhead for Pemlo - modern real estate business

I need a double sided business card design for Pemlo. Please see business card brief here https://files.quillnote-hub.net/page/7RtxQmZbn4LsWe2VyHoPk9dFjuC3gaXrTmqEi5Ns_pz/view?mode=shared

Please feel free to design the business cards however you feel best. I am happy to give some creative freedoms and then provide feedback from there.

Please then also create a letterhead to match the business card design

Colors

Designer to choose colors to be used in the design.

Requirements
Must have
• Must be a modern, elegant business card which looks very professional

```html
<!DOCTYPE html>
<html lang="en">
<head>
<meta charset="UTF-8">
<title>Pemlo</title>
<link rel="stylesheet" href="https://fonts.googleapis.com/css2?family=Orbitron:wght@500&display=swap">
<style>
  :root {
    --ink: #000000;
    --brand-red: #e30613;
    --band-dark: #2a0709;
    --band-mid: #4a0c10;
    --globe-deep: #041a2c;
    --globe-mid: #1d5579;
    --globe-light: #8cc3e0;
  }
  html, body {
    margin: 0;
    padding: 0;
    overflow: hidden;
    background: var(--ink);
  }
  .card {
    position: relative;
    width: 1200px;
    height: 686px;
    overflow: hidden;
    background: var(--ink);
  }
  .card-art {
    position: absolute;
    inset: 0;
    width: 1200px;
    height: 686px;
  }
  .brand-name {
    position: absolute;
    left: 40px;
    top: 222px;
    margin: 0;
    font-family: "Orbitron", sans-serif;
    font-weight: 500;
    font-size: 186px;
    line-height: 1;
    letter-spacing: 4px;
    text-transform: uppercase;
    color: var(--brand-red);
  }
</style>
</head>
<body>
  <main class="card">
    <svg class="card-art" viewBox="0 0 1200 686" xmlns="http://www.w3.org/2000/svg">
      <defs>
        <radialGradient id="globeGlow" cx="1150" cy="330" r="520" gradientUnits="userSpaceOnUse">
          <stop offset="0" stop-color="var(--globe-light)"/>
          <stop offset="0.45" stop-color="var(--globe-mid)"/>
          <stop offset="1" stop-color="var(--globe-deep)"/>
        </radialGradient>
        <linearGradient id="bandShade" x1="0" y1="0" x2="1" y2="0">
          <stop offset="0" stop-color="var(--band-dark)"/>
          <stop offset="1" stop-color="var(--band-mid)"/>
        </linearGradient>
      </defs>

      <rect class="globe-area" x="640" y="0" width="560" height="686" fill="url(#globeGlow)"
            role="img" aria-label="Glowing globe with a network of connected points"/>

      <path class="ink-panel" fill="var(--ink)"
            d="M0,0 H876 L1000,215 Q1015,245 1000,275 L667,686 H0 Z"/>

      <path class="accent-band" fill="url(#bandShade)"
            d="M876,0 H935 L1040,225 Q1052,255 1035,285 L700,686 H667 L1000,275 Q1015,245 1000,215 Z"/>

      <path class="accent-line" fill="none" stroke="var(--brand-red)" stroke-width="2.5"
            d="M981,0 L1080,230 Q1092,262 1075,292 L724,686"/>
    </svg>

    <h1 class="brand-name">Pemlo</h1>
  </main>
</body>
</html>
```